Business Identity Stationary

Already have the logo which is in the attached files so only need the Business STationary
1) Double Sided Business Card
2) Letterhead
3) Presentation folder with business card holder on inside cover
4) WIth compliments slip
See information for business cards, letterhead and presentation folder below.

This should be a simply job using a logo we already had designed along with a little device. I suggest using the device off center and perhaps lower in the corner in an abstract way. Also the logo device could be used as a watermark for the letterhead. The designer who created the logo presented something that I think works well for a business card. The front of the double sided business card could have the name logo small for the website address and only use the Lime device on the front. Then on the back could be the name Parvel Advisory logo.

Please note that for the business card the black and lime green background do look good. Also please think of using the lime device separately in an unusual way.

It has been brought to my attention that.my budget was far to low. Hopefully this.will attract you to the project. 

The parent company of Parvel Advisory is BrightHeron holdings. I have uploaded a file of the Bright Heron business card I really like. Perhaps use this business card as a guide to the type of modern and clean style I am looking for. It also works to have the Parvel Advisroy and Bright Heron similar.

Industry/Entity Type

Business

Font styles to use
Sans Serif

Colors
9bcb3c
000000
5c5c5c
add136
cadf82
eaf2cf
f9fbf2
1b1b1b
757575

Requirements
Must have
• 1) Double Sided Business Card
Renata Tolberg
Director
Tel: +505 8426 3057
Email: rtb@parveladvisory.com
Website: www.parveladvisory.com

Gregory Tolberg
Director
Tel: +505 8426 3092
Email: gkb@parveladvisory.com

Helena Pardo Duvignac
Director
Tel: 8342 1168
Email: hpd@parveladvisory.com

2) Letterhead
Logo
Lime Logo Device
Website Address: www.parveladvisory.com
Small print on bottom: Parvel Advisory a Bright Heron Holding Company SA. RUC K0470000283914

3) Presentation Folder
Traditional Presentation folder with inside front cover spot for the insertion of business card.

4) With Compliments slip

```html
<!DOCTYPE html>
<html lang="en">
<head>
<meta charset="utf-8">
<title>Parvel Advisory — Presentation Folder</title>
<link rel="stylesheet" href="https://fonts.googleapis.com/css2?family=PT+Sans&family=Questrial&display=swap">
<style>
  :root {
    --lime: #b3ff00;
    --lime-text: #add136;
    --panel: #0f1113;
    --stripe: #5c5c5c;
    --die: #e8782a;
    --white: #ffffff;
    --ink: #1b1b1b;
    --paper: #ffffff;
  }
  * { margin: 0; padding: 0; box-sizing: border-box; }
  html, body { width: 1200px; height: 898px; overflow: hidden; background: var(--paper); }
  .sheet { position: relative; width: 1200px; height: 898px; }
  .dieline { position: absolute; inset: 0; }
  .description {
    position: absolute; left: 231px; top: 66px;
    color: var(--white); font-family: "PT Sans", sans-serif;
  }
  .description h2 { font-weight: 400; font-size: 18px; letter-spacing: 0.2px; margin-bottom: 10px; }
  .description p { font-size: 11.2px; line-height: 19.5px; }
  .inner-mark {
    position: absolute; left: 360px; top: 296px; width: 120px; text-align: center;
    color: var(--white); font-family: "Questrial", sans-serif; font-size: 14px; letter-spacing: 1px;
  }
  .brand {
    position: absolute; left: 726px; top: 52px; width: 400px;
    color: var(--white); font-family: "Questrial", sans-serif; text-align: center;
  }
  .brand-name { font-size: 92px; line-height: 1; letter-spacing: 2px; }
  .brand-sub { font-size: 42px; letter-spacing: 15px; margin-top: 14px; text-transform: lowercase; }
  .contact {
    position: absolute; left: 236px; top: 675px;
    font-family: "PT Sans", sans-serif; font-size: 11.5px; color: var(--ink);
  }
  .contact-row { display: flex; align-items: center; height: 23px; }
  .contact-row svg { width: 20px; margin-right: 16px; }
  .web-divider { position: absolute; left: 430px; top: 676px; width: 3px; height: 36px; background: var(--ink); }
  .web {
    position: absolute; left: 448px; top: 676px;
    font-family: "Questrial", sans-serif; font-size: 27px; letter-spacing: 2.6px; color: var(--ink);
  }
</style>
</head>
<body>
<main class="sheet">
  <svg class="dieline" width="1200" height="898" viewBox="0 0 1200 898">
    <!-- flap and pocket fills -->
    <rect x="22" y="22" width="160" height="703" fill="var(--lime)"/>
    <rect x="182" y="725" width="489" height="152" fill="var(--lime)"/>
    <!-- cover panel -->
    <rect x="182" y="22" width="996" height="636" fill="var(--panel)"/>
    <rect x="182" y="656" width="996" height="6" fill="var(--stripe)"/>
    <rect x="182" y="662" width="996" height="63" fill="var(--lime)"/>
    <!-- end bars -->
    <rect x="1116" y="658" width="4" height="67" fill="var(--ink)"/>
    <rect x="1149" y="658" width="4" height="67" fill="var(--ink)"/>
    <rect x="1166" y="658" width="4" height="67" fill="var(--ink)"/>
    <!-- cut lines -->
    <g fill="none" stroke="var(--die)" stroke-width="1">
      <path d="M182 24 L120 24 Q32 30 30 130 L30 640 Q32 705 100 712 L150 722 L182 725"/>
      <line x1="112" y1="604" x2="160" y2="652"/>
      <path d="M182 725 L182 790 Q186 810 200 802 L194 808 L196 850 L240 848 Q250 856 300 864 L600 864 Q668 860 671 790 L671 725"/>
      <line x1="182" y1="22" x2="1178" y2="22"/>
      <line x1="1178" y1="22" x2="1178" y2="725"/>
      <line x1="671" y1="725" x2="1178" y2="725"/>
    </g>
    <!-- fold lines -->
    <g fill="none" stroke="var(--die)" stroke-width="1" stroke-dasharray="3 3">
      <line x1="182" y1="22" x2="182" y2="725"/>
      <line x1="680" y1="22" x2="680" y2="725"/>
      <line x1="182" y1="662" x2="680" y2="662"/>
      <line x1="182" y1="725" x2="671" y2="725"/>
    </g>
    <!-- crop marks -->
    <g stroke="#555" stroke-width="1">
      <line x1="22" y1="0" x2="22" y2="10"/><line x1="0" y1="22" x2="10" y2="22"/>
      <line x1="1178" y1="0" x2="1178" y2="10"/><line x1="1190" y1="22" x2="1200" y2="22"/>
      <line x1="22" y1="888" x2="22" y2="898"/><line x1="0" y1="877" x2="10" y2="877"/>
      <line x1="1178" y1="888" x2="1178" y2="898"/><line x1="1190" y1="877" x2="1200" y2="877"/>
    </g>
  </svg>

  <section class="description">
    <h2>DESCRIPTION TEXT</h2>
    <p>Lorem ipsum dolor sit amet, consectetur adipiscing elit.<br>
    Nos commodius agimus. Et quidem saepe quaerimus verbum Latinum par<br>
    Graeco et quod idem valeat; Et quidem Arcesilas tuus, etsi fuit in disserendo pertinacior,<br>
    tamen noster fuit; Aliter enim nosmet ipsos nosse non possumus.<br>
    Cur tantas regiones barbarorum pedibus obiit, tot maria transmisit?<br>
    Occultum facinus esse potuerit, gaudebit;</p>
  </section>

  <div class="inner-mark">Parvel Advisory</div>

  <header class="brand">
    <div class="brand-name">PARVEL</div>
    <div class="brand-sub">advisory</div>
  </header>

  <address class="contact" style="font-style:normal">
    <div class="contact-row">
      <svg viewBox="0 0 20 16" height="16"><path d="M3 2c2-1 3 0 4 2l-1 2c1 2 2 3 4 4l2-1c2 1 3 2 2 4-1 1-3 2-5 1C5 12 2 8 2 5c0-1 0-2 1-3z" fill="var(--ink)"/></svg>
      <span>+505 8426 3057</span>
    </div>
    <div class="contact-row">
      <svg viewBox="0 0 20 14" height="13"><rect x="1" y="1" width="18" height="12" fill="none" stroke="var(--ink)" stroke-width="2"/><path d="M1 1 L10 8 L19 1" fill="none" stroke="var(--ink)" stroke-width="2"/></svg>
      <span>rtb@parveladvisory.com</span>
    </div>
  </address>
  <div class="web-divider"></div>
  <div class="web">WWW.PARVELADVISORY.COM</div>
</main>
</body>
</html>
```